Website design and Setup for Real Estate Firm and Going Live

We are a commercial real estate investment firm and are looking for a 6 page website which is informational only. Some text and graphics on each page. We would want the designer to code and launch the website. This website needs to be corporate looking as well as innovative. We are setting up the website on webnook.

The first page will be a home page with generic commercial real estate look with a link to the following 5 pages on page 1. So page one (the Home Page should have a commercial real estate look with the text linking to the following pages. Page 2 "About Us" with 3 paragraphs describing our firm. Page 3 "Our Platform" with another few paragraphs on due diligence, acquisitions, financing, and management.

Page 4 is "Our Team" highlighting several manager profiles. Page 5 is our "investment Portfolio portal" which will be password protected so not a lot of text, only general graphics and anyone viewing the site casually won't get into the backend, Page 6 is the contact us page. All of the content will be uploaded shortly.

The project includes setting up hyperlinks in the website as well rotating images etc and a final complete live online product. We do not expect to pay for any stock images.

Target Market(s)

Investors, Real Estate Professionals, Brokerages

Industry/Entity Type

Real Estate

Coding

Coded - Design and coding required

Number of Pages Required

5+ page

Requirements
Must have
• Corporate cutting edge design, suitable for a financial corporation.

```html
<!DOCTYPE html>
<html lang="en">
<head>
<meta charset="utf-8">
<title>Meridian Holdings — Commercial Real Estate Investment</title>
<link rel="stylesheet" href="https://fonts.googleapis.com/css2?family=Rubik:wght@400;500&family=Zilla+Slab:wght@500;700&display=swap">
<style>
:root{
  --red:#dc1f3f;
  --ink:#1e1e1e;
  --text:#4a4a4a;
  --panel:#474747;
  --grey:#efefef;
  --navy:#141b2a;
  --blue-1:#1c4fb4;
  --blue-2:#7ea6e6;
  --white:#ffffff;
}
*{box-sizing:border-box;margin:0;padding:0}
html,body{width:1200px;height:3881px;overflow:hidden}
body{position:relative;background:var(--white);font-family:"Rubik",sans-serif;color:var(--text);font-size:14px}
.abs{position:absolute}
.btn{position:absolute;display:flex;align-items:center;justify-content:center;gap:7px;font-family:"Rubik",sans-serif;font-weight:500;font-size:13px;color:var(--white);border-radius:3px}
.btn svg{width:12px;height:12px}
.btn-red{background:var(--red)}
.btn-dark{background:#2e2e2e}
.eyebrow{font-size:13px;font-weight:500;letter-spacing:.3px;color:#555;text-transform:uppercase}

/* nav */
.nav{top:0;left:0;width:1200px;height:78px;background:var(--white)}
.brand{display:flex;align-items:center;gap:8px;font-family:"Zilla Slab",serif;font-weight:500;font-size:15px;color:#555;letter-spacing:.5px;white-space:nowrap}
.brand .mark{width:14px;height:14px;background:#8a8a8a}
.nav .brand{left:160px;top:28px}
.nav-links{left:384px;top:30px;display:flex;gap:21px;font-size:14px;color:#444}
.nav-links .active{color:var(--red);position:relative}
.nav-links .active::before{content:"";position:absolute;left:50%;top:-30px;width:2px;height:18px;background:var(--red)}
.nav .btn{left:830px;top:21px;width:210px;height:36px;background:#333}

/* hero */
.hero{top:78px;left:0;width:1200px;height:570px;background:linear-gradient(180deg,var(--blue-1) 0%,#3d73d2 45%,var(--blue-2) 100%);overflow:hidden}
.hero h1{position:absolute;top:130px;width:1200px;text-align:center;font-family:"Zilla Slab",serif;font-weight:700;font-size:54px;line-height:58px;color:#f4f6fa}
.hero .btn{left:535px;top:267px;width:130px;height:41px}
.call-box{position:absolute;left:479px;top:416px;width:229px;height:67px;background:#2a2a2a;clip-path:polygon(6% 0,100% 0,100% 100%,0 100%)}
.call-box .ico{position:absolute;left:34px;top:13px;width:42px;height:42px;border-radius:50%;background:var(--white);display:flex;align-items:center;justify-content:center}
.call-box .ico svg{width:20px;height:20px}
.call-box .lbl{position:absolute;left:90px;top:15px;font-size:11px;color:#ddd}
.call-box .num{position:absolute;left:90px;top:31px;font-size:16px;font-weight:500;color:var(--white);letter-spacing:.5px}
.hero-curve{position:absolute;left:0;bottom:0;width:1200px;height:110px}

/* who we are */
.who-label{left:160px;top:670px}
.who-title{left:160px;top:706px;font-family:"Zilla Slab",serif;font-weight:700;font-size:40px;line-height:46px;color:var(--ink)}
.stat{top:726px;text-align:center;width:160px}
.stat b{font-family:"Zilla Slab",serif;font-weight:700;font-size:68px;line-height:70px;color:var(--ink)}
.stat sup{font-family:"Rubik",sans-serif;font-size:30px;font-weight:400;vertical-align:top;position:relative;top:-6px;color:var(--ink)}
.stat span{display:block;font-size:15px;color:#333;margin-top:2px}
.about-panel{left:665px;top:926px;width:535px;height:411px;background:var(--panel)}
.about-strip{left:314px;top:1292px;width:351px;height:45px;background:var(--panel)}
.photo{background:linear-gradient(135deg,#c9c5bd,#8c8780 60%,#5f5b55)}
.about-photo{left:160px;top:883px;width:505px;height:409px;box-shadow:0 4px 12px rgba(0,0,0,.12)}
.about-copy{left:706px;top:980px;width:380px;color:#f1f1f1}
.about-copy h3{font-family:"Zilla Slab",serif;font-weight:700;font-size:23px;color:var(--white);margin-bottom:8px}
.about-copy p{font-size:14.5px;line-height:22px;margin-bottom:31px}
.about-copy + .btn{left:707px;top:1239px;width:158px;height:38px}

/* platform */
.platform-label{left:0;top:1459px;width:1200px;text-align:center}
.platform-title{left:0;top:1480px;width:1200px;text-align:center;font-family:"Zilla Slab",serif;font-weight:700;font-size:41px;color:var(--ink)}
.platform-lead{left:0;top:1533px;width:1200px;text-align:center;font-size:14.5px;line-height:22px;color:#555}
.platform-band{left:0;top:1693px;width:1200px;height:469px;background:var(--grey)}
.card{position:absolute;top:1614px;width:280px;height:421px;background:var(--white);box-shadow:0 3px 10px rgba(0,0,0,.08);overflow:hidden}
.card .img{height:165px}
.card h3{margin:28px 0 0 24px;font-family:"Zilla Slab",serif;font-weight:700;font-size:22px;color:var(--red)}
.card p{margin:8px 0 0 24px;width:235px;font-size:14.5px;line-height:24px;color:#555}
.card .plus{position:absolute;left:24px;top:334px;width:38px;height:38px;border-radius:50%;background:#555;display:flex;align-items:center;justify-content:center}
.card .plus svg{width:12px;height:12px}
.card .arc{position:absolute;left:0;bottom:0;width:280px;height:36px}
.img-deal{background:linear-gradient(135deg,#8fa8c6,#3f5b80 55%,#1f3250)}
.img-review{background:linear-gradient(135deg,#b8a48a,#5e6f6b 55%,#2d4a45)}
.img-finance{background:linear-gradient(135deg,#e7b877,#b97b47 55%,#7a4a2c)}
.platform-band + .btn{left:514px;top:2071px;width:172px;height:39px}

/* team */
.team{left:0;top:2162px;width:1200px;height:651px;background:linear-gradient(120deg,#2459c4 0%,#3d6fd1 50%,#8aa9d8 100%)}
.team-label{left:160px;top:2213px;color:#eaf0fb}
.team-title{left:160px;top:2234px;font-family:"Zilla Slab",serif;font-weight:700;font-size:38px;letter-spacing:1px;color:var(--white)}
.team-btn{left:858px;top:2225px;width:181px;height:39px}
.member{position:absolute;width:431px;height:211px}
.member .portrait{position:absolute;left:0;top:0;width:194px;height:211px;border:4px solid var(--white);background:linear-gradient(180deg,#9aa0a8,#3a3d44)}
.member .info{position:absolute;left:194px;top:31px;width:237px;height:180px;background:var(--white);padding:18px 0 0 16px}
.member h3{font-family:"Zilla Slab",serif;font-weight:700;font-size:23px;color:var(--red);line-height:26px}
.member .role{font-size:12.5px;color:#333;letter-spacing:.3px;margin-top:1px}
.member .rule{width:32px;height:2px;background:var(--red);margin-top:5px}
.member p{font-size:14.5px;line-height:22px;color:#555;margin-top:10px}
.member .social{display:flex;gap:20px;margin-top:12px}
.member .social i{width:8px;height:8px;border-radius:50%;background:#777;display:block}

/* contact */
.touch{left:0;top:2864px;width:740px;height:498px;background:var(--red);overflow:hidden}
.touch h2{position:absolute;left:160px;top:42px;font-family:"Zilla Slab",serif;font-weight:700;font-size:41px;color:var(--white)}
.touch .lead{position:absolute;left:160px;top:90px;width:440px;font-size:14.5px;line-height:23px;color:#fde8ec}
.field{position:absolute;background:var(--white);border:1px solid #eee;font-size:13px;color:#888;padding:12px 12px}
.touch .btn{left:160px;top:409px;width:155px;height:39px}
.contact-card{left:684px;top:2914px;width:356px;height:406px;background:#eeeeee}
.contact-card h2{position:absolute;left:54px;top:32px;font-family:"Zilla Slab",serif;font-weight:700;font-size:40px;color:var(--ink)}
.c-item{position:absolute;left:58px;display:flex;gap:20px}
.c-ico{width:56px;height:56px;border-radius:50%;border:2px solid var(--red);background:var(--white);display:flex;align-items:center;justify-content:center;flex:none;box-shadow:0 0 0 4px #eeeeee,0 0 0 5px #f5c5cf}
.c-ico svg{width:24px;height:24px}
.c-item .lbl{font-size:14px;color:#444;line-height:21px}
.c-item .val{font-size:15px;color:#222;line-height:21px}
.portal-link{position:absolute;left:58px;top:351px;font-size:13px;font-weight:500;color:#222;text-decoration:underline;display:flex;align-items:center;gap:6px}
.portal-link svg{width:12px;height:12px}

/* footer */
.footer-curve{left:0;top:3390px;width:1200px;height:130px}
.footer{left:0;top:3470px;width:1200px;height:411px;background:var(--navy)}
.footer .brand{position:absolute;left:160px;top:190px;color:var(--white);font-size:17px;letter-spacing:.5px}
.footer .brand .mark{width:16px;height:16px;background:var(--white)}
.socials{position:absolute;left:160px;top:248px;display:flex;gap:10px}
.socials i{width:40px;height:40px;border-radius:50%;background:var(--red);display:block}
.f-col{position:absolute;top:87px;color:#e4e6ea}
.f-col h4{font-family:"Zilla Slab",serif;font-weight:700;font-size:21px;color:var(--white);margin-bottom:14px}
.f-col li{list-style:none;font-size:14.5px;line-height:34px}
.f-row{display:flex;gap:10px;font-size:14.5px;line-height:21px;margin-bottom:20px}
.f-row svg{width:13px;height:13px;flex:none;margin-top:4px}
.f-col .sub{font-size:13.5px;line-height:22px;width:240px}
.f-col .email{position:absolute;left:1px;top:95px;width:225px;height:38px;background:var(--white);font-size:13px;color:#666;padding:11px 12px}
.f-col .btn{left:1px;top:148px;width:224px;height:38px}
.copy{position:absolute;left:0;top:354px;width:1200px;text-align:center;font-family:"Zilla Slab",serif;font-size:14px;color:#9aa0ab}
.copy b{color:#d4d7dd;font-weight:500}
</style>
</head>
<body>

<!-- navigation -->
<header class="abs nav">
  <div class="abs brand"><span class="mark"></span>MERIDIAN HOLDINGS</div>
  <nav class="abs nav-links">
    <span class="active">Home</span><span>About Us</span><span>Our Platform</span><span>Our Team</span><span>Contact Us</span>
  </nav>
  <a class="btn">Investment Portfolio Portal</a>
</header>

<!-- hero -->
<section class="abs hero" role="img" aria-label="Upward view of glass office towers against a blue sky">
  <h1>A Commercial Real<br>Estate Investment Firm</h1>
  <a class="btn btn-red">Find More
    <svg viewBox="0 0 12 12"><path d="M1 6h9M6.5 2.5 10 6l-3.5 3.5" stroke="#fff" stroke-width="1.8" fill="none"/></svg></a>
  <div class="call-box">
    <div class="ico"><svg viewBox="0 0 24 24"><path d="M6 3l3 4-2 2c1 2.5 3.5 5 6 6l2-2 4 3-2 3C10 19 5 14 3 6z" fill="none" stroke="#dc1f3f" stroke-width="1.6"/></svg></div>
    <div class="lbl">Call Us Now:</div>
    <div class="num">123-456-7890</div>
  </div>
  <svg class="hero-curve" viewBox="0 0 1200 110" preserveAspectRatio="none">
    <path d="M0 110 Q600 -20 1200 110 Z" fill="#dc1f3f"/>
    <path d="M0 110 Q600 10 1200 110 Z" fill="#fff"/>
  </svg>
</section>

<!-- who we are -->
<div class="abs eyebrow who-label">Who We Are</div>
<h2 class="abs who-title">We invest quality<br>infrastructure &amp; real estate<br>project since 2001</h2>
<div class="abs stat" style="left:740px"><b>55</b><sup>+</sup><span>Completed Project</span></div>
<div class="abs stat" style="left:900px"><b>20</b><sup>+</sup><span>Award Winning</span></div>

<div class="abs about-panel"></div>
<div class="abs about-strip"></div>
<div class="abs photo about-photo" role="img" aria-label="Business team gathered around a laptop in a bright office"></div>
<div class="abs about-copy">
  <h3>Our Mission</h3>
  <p>Lorem ipsum dolor sit amet consectetur viverra adipiscing elit sed do eiusmod tempor lacus vel incididunt ut labore et dolore magna aliqua.</p>
  <h3>Our Vision</h3>
  <p>Lorem ipsum dolor sit amet consectetur viverra adipiscing elit sed do eiusmod tempor lacus vel incididunt ut labore et dolore magna aliqua.</p>
</div>
<a class="btn btn-red">More About Us
  <svg viewBox="0 0 12 12"><path d="M1 6h9M6.5 2.5 10 6l-3.5 3.5" stroke="#fff" stroke-width="1.8" fill="none"/></svg></a>

<!-- platform -->
<div class="abs eyebrow platform-label">What We Do</div>
<h2 class="abs platform-title">Our Platform</h2>
<p class="abs platform-lead">Lorem ipsum dolor sit amet consectetur viverra adipiscing<br>elit sed do eiusmod tempor lacus vel incididunt ut</p>
<div class="abs platform-band"></div>
<a class="btn btn-dark">View All Services
  <svg viewBox="0 0 12 12"><path d="M1 6h9M6.5 2.5 10 6l-3.5 3.5" stroke="#fff" stroke-width="1.8" fill="none"/></svg></a>

<article class="card" style="left:160px">
  <div class="img img-deal" role="img" aria-label="Handshake over signed documents"></div>
  <h3>Acquisitions</h3>
  <p>Excepteur sint occaecat undere cupidatat non proident sunt sid total culpa qui officia deserunt mollit anim id est laborum vol..</p>
  <span class="plus"><svg viewBox="0 0 12 12"><path d="M6 1v10M1 6h10" stroke="#fff" stroke-width="2"/></svg></span>
  <svg class="arc" viewBox="0 0 280 36"><path d="M0 36 Q140 -14 280 36 Q140 2 0 36Z" fill="#dc1f3f"/></svg>
</article>
<article class="card" style="left:460px">
  <div class="img img-review" role="img" aria-label="Professional reviewing files in a modern office"></div>
  <h3>Due Diligence</h3>
  <p>Excepteur sint occaecat undere cupidatat non proident sunt sid total culpa qui officia deserunt mollit anim id est laborum vol..</p>
  <span class="plus"><svg viewBox="0 0 12 12"><path d="M6 1v10M1 6h10" stroke="#fff" stroke-width="2"/></svg></span>
  <svg class="arc" viewBox="0 0 280 36"><path d="M0 36 Q140 -14 280 36 Q140 2 0 36Z" fill="#dc1f3f"/></svg>
</article>
<article class="card" style="left:760px">
  <div class="img img-finance" role="img" aria-label="Hands working a calculator beside financial papers"></div>
  <h3>Financing</h3>
  <p>Excepteur sint occaecat undere cupidatat non proident sunt sid total culpa qui officia deserunt mollit anim id est laborum vol..</p>
  <span class="plus"><svg viewBox="0 0 12 12"><path d="M6 1v10M1 6h10" stroke="#fff" stroke-width="2"/></svg></span>
  <svg class="arc" viewBox="0 0 280 36"><path d="M0 36 Q140 -14 280 36 Q140 2 0 36Z" fill="#dc1f3f"/></svg>
</article>

<!-- team -->
<section class="abs team" role="img" aria-label="Modern residential towers with planted balconies under a blue sky"></section>
<div class="abs eyebrow team-label">Meet Our Professionals</div>
<h2 class="abs team-title">EXECUTIVE TEAM</h2>
<a class="btn btn-red team-btn">View All Members
  <svg viewBox="0 0 12 12"><path d="M1 6h9M6.5 2.5 10 6l-3.5 3.5" stroke="#fff" stroke-width="1.8" fill="none"/></svg></a>

<div class="member" style="left:160px;top:2318px">
  <div class="portrait" role="img" aria-label="Portrait of Daniel Roark"></div>
  <div class="info"><h3>Daniel Roark</h3><div class="role">FINANCE MANAGER</div><div class="rule"></div>
    <p>Lorem ipsum dolor sit amet consectetur viverra elit se.</p><div class="social"><i></i><i></i><i></i><i></i></div></div>
</div>
<div class="member" style="left:609px;top:2318px">
  <div class="portrait" role="img" aria-label="Portrait of Clara Whitfield"></div>
  <div class="info"><h3>Clara Whitfield</h3><div class="role">DIRECTOR MANAGER</div><div class="rule"></div>
    <p>Lorem ipsum dolor sit amet consectetur viverra elit se.</p><div class="social"><i></i><i></i><i></i><i></i></div></div>
</div>
<div class="member" style="left:160px;top:2549px">
  <div class="portrait" role="img" aria-label="Portrait of Marcus Hale"></div>
  <div class="info"><h3>Marcus Hale</h3><div class="role">INVESTMENT OFFICER</div><div class="rule"></div>
    <p>Lorem ipsum dolor sit amet consectetur viverra elit se.</p><div class="social"><i></i><i></i><i></i><i></i></div></div>
</div>
<div class="member" style="left:609px;top:2549px">
  <div class="portrait" role="img" aria-label="Portrait of Lena Osei"></div>
  <div class="info"><h3>Lena Osei</h3><div class="role">FINANCE MANAGER</div><div class="rule"></div>
    <p>Lorem ipsum dolor sit amet consectetur viverra elit se.</p><div class="social"><i></i><i></i><i></i><i></i></div></div>
</div>

<!-- contact -->
<section class="abs touch">
  <h2>Get In Touch</h2>
  <p class="lead">Lorem ipsum dolor sit amet consectetur viverra adipiscing elit sed do eiusmod tempor lacus.</p>
  <div class="field" style="left:160px;top:154px;width:237px;height:39px">First Name</div>
  <div class="field" style="left:409px;top:154px;width:238px;height:39px">Last Name</div>
  <div class="field" style="left:160px;top:207px;width:237px;height:39px">Email Address</div>
  <div class="field" style="left:409px;top:207px;width:238px;height:39px">Phone Number</div>
  <div class="field" style="left:160px;top:258px;width:487px;height:134px">Leave Your Message</div>
  <a class="btn btn-dark">Send Message
    <svg viewBox="0 0 12 12"><path d="M1 6h9M6.5 2.5 10 6l-3.5 3.5" stroke="#fff" stroke-width="1.8" fill="none"/></svg></a>
</section>
<section class="abs contact-card">
  <h2>Contact Us</h2>
  <div class="c-item" style="top:103px">
    <span class="c-ico"><svg viewBox="0 0 24 24"><path d="M6 3l3 4-2 2c1 2.5 3.5 5 6 6l2-2 4 3-2 3C10 19 5 14 3 6z" fill="none" stroke="#dc1f3f" stroke-width="1.6"/></svg></span>
    <div><div class="lbl">Call Us Now:</div><div class="val">123-456-7890</div></div>
  </div>
  <div class="c-item" style="top:186px">
    <span class="c-ico"><svg viewBox="0 0 24 24"><path d="M12 22s7-7 7-12a7 7 0 0 0-14 0c0 5 7 12 7 12z" fill="none" stroke="#dc1f3f" stroke-width="1.6"/><circle cx="12" cy="10" r="2.5" fill="none" stroke="#dc1f3f" stroke-width="1.6"/></svg></span>
    <div><div class="lbl">Our Address:</div><div class="val">48 Linden Ave.<br>Harlow, CT 06402</div></div>
  </div>
  <div class="c-item" style="top:272px">
    <span class="c-ico"><svg viewBox="0 0 24 24"><rect x="3" y="6" width="18" height="12" fill="none" stroke="#dc1f3f" stroke-width="1.6"/><path d="M3 6l9 7 9-7" fill="none" stroke="#dc1f3f" stroke-width="1.6"/></svg></span>
    <div><div class="lbl">Mail Us:</div><div class="val">info@meridianholdings.com</div></div>
  </div>
  <a class="portal-link">Go to Investment Portfolio Portal
    <svg viewBox="0 0 12 12"><rect x="2" y="5" width="8" height="6" fill="#222"/><path d="M3.5 5V3.5a2.5 2.5 0 0 1 5 0V5" fill="none" stroke="#222" stroke-width="1.4"/></svg></a>
</section>

<!-- footer -->
<svg class="abs footer-curve" viewBox="0 0 1200 130" preserveAspectRatio="none">
  <path d="M0 20 Q600 150 1200 20 L1200 130 L0 130Z" fill="#8d8f94"/>
  <path d="M0 40 Q600 160 1200 40 L1200 130 L0 130Z" fill="#141b2a"/>
</svg>
<footer class="abs footer">
  <div class="brand"><span class="mark"></span>MERIDIAN HOLDINGS</div>
  <div class="socials"><i></i><i></i><i></i><i></i></div>

  <div class="f-col" style="left:402px">
    <h4>Quick Links</h4>
    <ul><li>Home</li><li>About Us</li><li>Our Platform</li><li>Our Team</li><li>Contact Us</li></ul>
  </div>
  <div class="f-col" style="left:570px">
    <h4>Contact Info</h4>
    <div class="f-row"><svg viewBox="0 0 24 24"><path d="M12 22s7-7 7-12a7 7 0 0 0-14 0c0 5 7 12 7 12z" fill="#dc1f3f"/><circle cx="12" cy="10" r="2.5" fill="#141b2a"/></svg><div>48 Linden Ave.<br>Harlow, CT 06402</div></div>
    <div class="f-row"><svg viewBox="0 0 24 24"><path d="M6 3l3 4-2 2c1 2.5 3.5 5 6 6l2-2 4 3-2 3C10 19 5 14 3 6z" fill="#dc1f3f"/></svg><div>Phone:<br>123-456-7890</div></div>
    <div class="f-row"><svg viewBox="0 0 24 24"><rect x="3" y="6" width="18" height="13" fill="#dc1f3f"/><path d="M3 6l9 7 9-7" fill="none" stroke="#141b2a" stroke-width="1.6"/></svg><div>Email:<br>info@meridianholdings.com</div></div>
  </div>
  <div class="f-col" style="left:814px">
    <h4>Subscribe Newsletter</h4>
    <p class="sub">Subscribe our newsletter get<br>latest updated</p>
    <div class="email">Email Address.</div>
    <a class="btn btn-red">Subscribe Us
      <svg viewBox="0 0 12 12"><path d="M1 5.5 11 1 8 11 6 7z" fill="none" stroke="#fff" stroke-width="1.3"/></svg></a>
  </div>
  <p class="copy">Copyright © 2021 <b>Meridian Holdings.</b> All rights reserved.</p>
</footer>

</body>
</html>
```